Motivation health and wellbeing counselling. 'Bloom in bold' Blossom into newness' Glowing Just Within'

I need a design for my a new buisness aimed at women in the middle age range. Motivational coaching and counselling for weight loss, depression and anxiety and other mental health conditions, addiction, loss of confidence, menopause, empty nest syndrome and other life changing events. Experienced qualified counsellor with a lived experience to provide 1:1 counselling as well as the option for group sessions and social media online support. Long term sustainable change goals to support persistant progress in exercise, healthy eating and positive lifestyle changes. The card should promote a somewhat funky feminine positive message. I would like to trial the colours magenta, red, yellow and a bold blue or green.

```html
<!DOCTYPE html>
<html lang="en">
<head>
<meta charset="utf-8">
<title>Counselling Business Card</title>
<link rel="stylesheet" href="https://fonts.googleapis.com/css2?family=Open+Sans:wght@400;600&display=swap">
<style>
  :root {
    --stage: #8a8a8a;
    --sky-magenta: #cf6aa6;
    --sky-pink: #e79aa8;
    --sky-peach: #f6c98e;
    --sun-glow: #fff6d8;
    --horizon-orange: #f0a33c;
    --horizon-deep: #e68a2a;
    --topic-ink: rgba(214, 110, 120, 0.55);
    --service-ink: rgba(170, 160, 160, 0.6);
    --contact-ink: #1f1a1c;
    --mark-ink: rgba(255, 255, 255, 0.6);
  }
  * { box-sizing: border-box; margin: 0; padding: 0; }
  html, body {
    width: 1200px; height: 1000px; overflow: hidden;
    background: var(--stage);
  }
  .card {
    position: absolute;
    left: 100px; top: 214px;
    width: 1000px; height: 572px;
    border-radius: 22px;
    overflow: hidden;
    font-family: "Open Sans", Arial, sans-serif;
    box-shadow: 0 18px 40px rgba(0,0,0,0.35);
  }
  .card__photo {
    position: absolute; inset: 0;
    background:
      radial-gradient(circle at 48% 60%, var(--sun-glow) 0%, rgba(255,246,216,0.85) 14%, rgba(255,230,170,0) 40%),
      linear-gradient(180deg, var(--sky-magenta) 0%, var(--sky-pink) 28%, var(--sky-peach) 55%, var(--horizon-orange) 82%, var(--horizon-deep) 100%);
  }
  .card__topics {
    position: absolute; left: 330px; top: 60px;
    font-weight: 600; font-size: 34px; line-height: 36px;
    color: var(--topic-ink);
    white-space: nowrap;
  }
  .card__topics span { display: block; }
  .card__topics span:nth-child(2) { padding-left: 92px; }
  .card__topics span:nth-child(3) { padding-left: 176px; }
  .card__topics span:nth-child(4) { padding-left: 236px; }
  .card__mark {
    position: absolute; right: 40px; top: 92px;
    font-weight: 600; font-size: 34px; line-height: 40px;
    white-space: nowrap;
    color: var(--mark-ink);
  }
  .card__service {
    position: absolute;
    font-weight: 600; font-size: 36px;
    white-space: nowrap;
    color: var(--service-ink);
  }
  .card__service--counselling { left: 360px; top: 300px; }
  .card__service--motivation { left: 380px; top: 390px; }
  .card__contact {
    position: absolute; left: 628px; top: 318px;
    display: flex; align-items: center; gap: 12px;
    white-space: nowrap;
    color: var(--contact-ink);
  }
  .card__phone-icon { width: 50px; height: 50px; flex: none; }
  .card__name { font-size: 30px; font-weight: 400; line-height: 32px; }
  .card__role, .card__number { font-size: 15px; line-height: 17px; font-weight: 600; }
</style>
</head>
<body>
  <section class="card">
    <div class="card__photo" role="img" aria-label="Sunset sky photograph with a woman silhouetted, arms stretched behind her"></div>

    <div class="card__topics">
      <span>depression</span>
      <span>anxiety</span>
      <span>addiction</span>
      <span>menopause</span>
    </div>

    <div class="card__mark">Bloom in bold</div>

    <div class="card__service card__service--counselling">Counselling</div>
    <div class="card__service card__service--motivation">Motivation</div>

    <div class="card__contact">
      <svg class="card__phone-icon" viewBox="0 0 50 50" aria-hidden="true">
        <path d="M25 4a20 20 0 1 0 10 37.3L45 46l-3.5-9.5A20 20 0 0 0 25 4z" fill="none" stroke="#1f1a1c" stroke-width="3" stroke-linejoin="round"/>
        <path d="M18 15c1.5-1 3-1 3.8.4l1.8 3.4c.5 1-.1 2-1 2.6l-1 .7c1 2.6 3 4.7 5.5 5.8l.8-1c.7-.9 1.7-1.3 2.7-.8l3.3 1.9c1.3.8 1.200 2.4.2 3.7-1.5 1.9-3.7 2.3-6 1.2-4.8-2.3-8.6-6.3-10.6-11.2-.8-2.4-.9-4.8.5-6.7z" fill="#1f1a1c"/>
      </svg>
      <div class="card__details">
        <div class="card__name">Dr. Lena Marsh</div>
        <div class="card__role">Women's Health Specialists</div>
        <div class="card__number">+343-5550142876</div>
      </div>
    </div>
  </section>
</body>
</html>
```